Lustiges Einladungskarten-Design für Feier gesucht
Zielgruppe
private Einladung
Aufgabenstellung
Einladung im Posterformat DIN A2 dass auf DINA A6 (9 einzelne Felder) runter gefaltet werden kann.
Die Einladung soll lustig, witzig und ausgefallen sein - auf keinen Fall klassisch, schnörkelig, spießig.
Die Location soll genannt werden: eine bewirtete Waldhütte im Sauerland, Übernachtungsmöglichkeiten, Beginn der Feier: 18.30 Uhr am 29.09.2018
Es handelt sich um eine Feier zum 50.Geburtstag, zum 46. Geburtstag, zur Hochzeit – aber vor allem feiern wir die das Leben, die Liebe und unsere Freunde.
Es ist eine Grillparty – kein Dresscode, keine Spiele – sondern essen, trinken, feiern, tanzen, Spaß haben.
Gern handlettering , illustriert oder andere kreative Ideen.

```html
<!DOCTYPE html>
<html lang="de">
<head>
<meta charset="utf-8">
<title>Einladung – Bist du Wald?</title>
<link href="https://fonts.googleapis.com/css2?family=Amatic+SC:wght@400;700&display=swap" rel="stylesheet">
<style>
  :root {
    --outer: #e3e3dd;
    --frame: #ffffff;
    --panel: #e1e2dc;
    --ink: #3d3330;
    --green: #a5c737;
    --yellow: #fdd22b;
  }
  * { margin: 0; padding: 0; box-sizing: border-box; }
  html, body { width: 849px; height: 1200px; overflow: hidden; background: var(--outer); }
  .poster {
    position: relative; width: 849px; height: 1200px;
    background: var(--outer);
    font-family: "Amatic SC", cursive;
    color: var(--ink);
  }
  .frame {
    position: absolute; left: 12px; top: 17px; width: 825px; height: 1166px;
    background: var(--frame);
  }
  .sheet {
    position: absolute; left: 53px; top: 75px; width: 743px; height: 1049px;
    background: var(--panel);
  }
  .t { position: absolute; line-height: 1; font-weight: 700; white-space: nowrap; }
  .accent { color: var(--green); }
  .small { font-weight: 700; font-size: 19px; line-height: 1.05; }
  .art { position: absolute; border-radius: 8px; }
  .art.green { background: var(--green); }
  .art.mix { background: linear-gradient(135deg, var(--green), var(--ink)); }
  .art.dark { background: linear-gradient(160deg, var(--ink), #6b5f55); }
  .arrow { position: absolute; overflow: visible; }
  .rot { transform-origin: center; transform: rotate(-90deg); }
</style>
</head>
<body>
<main class="poster">
  <div class="frame"></div>

  <!-- Feld 1 -->
  <div class="t" style="left:86px;top:96px;font-size:140px;">B<span class="accent">i</span>st</div>
  <div class="art green" role="img" aria-label="Gezeichnete Tanne" style="left:68px;top:220px;width:50px;height:82px;"></div>
  <div class="t" style="left:124px;top:206px;font-size:110px;"><span class="accent">d</span>u</div>
  <div class="art mix" role="img" aria-label="Gezeichneter Laubbaum" style="left:226px;top:218px;width:56px;height:78px;border-radius:40% 40% 8px 8px;"></div>
  <div class="t" style="left:74px;top:300px;font-size:110px;">wal<span class="accent">d</span>?</div>

  <!-- Feld 2 -->
  <div class="t" style="left:320px;top:108px;font-size:62px;"><span class="accent">d</span>ann zieh <span class="accent">a</span>n</div>
  <div class="t" style="left:320px;top:172px;font-size:50px;">was <span class="accent">d</span>u willst!</div>
  <div class="art mix" role="img" aria-label="Gezeichnetes T-Shirt" style="left:320px;top:230px;width:108px;height:86px;"></div>
  <div class="art green" role="img" aria-label="Gezeichnete Krone" style="left:458px;top:225px;width:48px;height:46px;"></div>
  <div class="art mix" role="img" aria-label="Gezeichnete Fliege" style="left:436px;top:272px;width:82px;height:46px;"></div>
  <div class="t" style="left:329px;top:326px;font-size:72px;">o<span class="accent">d</span>er nix</div>

  <!-- Feld 3 -->
  <div class="t" style="left:567px;top:92px;font-size:46px;">egal wie</div>
  <div class="art green" role="img" aria-label="Gezeichneter Kompass" style="left:717px;top:99px;width:32px;height:32px;border-radius:50%;"></div>
  <div class="t" style="left:566px;top:128px;font-size:54px;"><span class="accent">a</span>ber komm zur</div>
  <div class="art green" role="img" aria-label="Gezeichnetes Flugzeug, Auto und Fahrrad" style="left:572px;top:199px;width:197px;height:52px;"></div>
  <div class="t" style="left:567px;top:266px;font-size:58px;">wal<span class="accent">d</span>hütte im</div>
  <div class="t" style="left:566px;top:312px;font-size:66px;">sauerlan<span class="accent">d</span></div>

  <!-- Feld 4 -->
  <div class="art green" role="img" aria-label="Gezeichneter Setzling" style="left:85px;top:451px;width:40px;height:56px;"></div>
  <div class="t" style="left:139px;top:452px;font-size:64px;">leben</div>
  <div class="t" style="left:72px;top:520px;font-size:64px;"><span class="accent">ii</span> freun<span class="accent">d</span>e</div>
  <svg class="arrow" style="left:85px;top:598px;" width="46" height="42" viewBox="0 0 46 42" aria-hidden="true">
    <path d="M23 40 C10 30 2 22 2 13 C2 6 7 2 12 2 C17 2 21 5 23 9 C25 5 29 2 34 2 C39 2 44 6 44 13 C44 22 36 30 23 40Z" fill="var(--green)" stroke="var(--ink)" stroke-width="2.5"/>
  </svg>
  <div class="t" style="left:146px;top:590px;font-size:64px;">liebe</div>
  <div class="t small" style="left:84px;top:674px;">wenn dir noch ein weiterer<br>grund zum feiern einfällt</div>
  <div class="t" style="left:86px;top:708px;font-size:34px;">bring ihn mit!!</div>

  <!-- Feld 5 -->
  <div class="art green" role="img" aria-label="Gezeichneter Vogel auf einem Nest" style="left:395px;top:463px;width:65px;height:60px;border-radius:50% 50% 10px 10px;"></div>
  <div class="t rot" style="left:313px;top:600px;width:220px;text-align:center;font-size:100px;">18.30</div>

  <!-- Feld 6 -->
  <div class="t" style="left:569px;top:460px;font-size:58px;"><span class="accent">a</span>m besten</div>
  <div class="t" style="left:569px;top:518px;font-size:46px;"><span class="accent">a</span>m 29.9.2018</div>
  <div class="art green" role="img" aria-label="Gezeichneter Kalender mit dem 29. Sept 2018" style="left:630px;top:591px;width:76px;height:91px;border-radius:3px;"></div>
  <svg class="arrow" style="left:590px;top:716px;" width="12" height="29" viewBox="0 0 12 29" aria-hidden="true">
    <circle cx="6" cy="9" r="5" fill="var(--green)" stroke="var(--ink)" stroke-width="1.2"/>
    <rect x="3.5" y="15" width="5" height="6" fill="var(--ink)"/>
  </svg>
  <div class="t" style="left:606px;top:723px;font-size:17px;">denn da sind auch die anderen da</div>

  <!-- Feld 7 -->
  <div class="t small" style="left:70px;top:804px;font-size:20px;">du findest dein auto nicht mehr?<br>oder hast plötzlich 2 davon?</div>
  <div class="art green" role="img" aria-label="Zwei gezeichnete Autos" style="left:105px;top:865px;width:138px;height:39px;"></div>
  <div class="t" style="left:66px;top:922px;font-size:48px;"><span class="accent">d</span>ann übernachte</div>
  <div class="t" style="left:80px;top:964px;font-size:48px;">besser hier!</div>
  <div class="art mix" role="img" aria-label="Gezeichnete Reisetasche und Häuschen" style="left:109px;top:1017px;width:131px;height:73px;"></div>

  <!-- Feld 8 -->
  <div class="art green" role="img" aria-label="Gezeichnete Hand, die nach unten zeigt" style="left:345px;top:818px;width:60px;height:86px;"></div>
  <div class="t" style="left:336px;top:916px;font-size:48px;">essen</div>
  <div class="t" style="left:336px;top:976px;font-size:48px;">feiern</div>
  <div class="t" style="left:336px;top:1044px;font-size:48px;">trinken</div>
  <div class="t rot" style="left:348px;top:921px;width:280px;text-align:center;font-size:70px;">spaß haben</div>

  <!-- Feld 9 -->
  <div class="art dark" role="img" aria-label="Gezeichnetes Fernglas mit kleinem Vogel" style="left:646px;top:878px;width:52px;height:84px;"></div>
  <div class="t" style="left:606px;top:976px;font-size:50px;">see you</div>

  <!-- Pfeile -->
  <svg class="arrow" style="left:251px;top:397px;" width="84" height="56" viewBox="0 0 84 56" aria-hidden="true">
    <path d="M3 16 L46 14 L46 2 L81 28 L46 54 L46 40 L3 40 Z" fill="var(--yellow)" stroke="var(--ink)" stroke-width="3" stroke-linejoin="round"/>
  </svg>
  <svg class="arrow" style="left:528px;top:379px;" width="58" height="84" viewBox="0 0 58 84" aria-hidden="true">
    <path d="M16 3 L40 3 L42 44 L56 44 L29 81 L2 44 L16 44 Z" fill="var(--yellow)" stroke="var(--ink)" stroke-width="3" stroke-linejoin="round"/>
  </svg>
  <svg class="arrow" style="left:517px;top:635px;" width="84" height="58" viewBox="0 0 84 58" aria-hidden="true">
    <path d="M81 18 L38 16 L38 3 L3 29 L38 55 L38 42 L81 40 Z" fill="var(--yellow)" stroke="var(--ink)" stroke-width="3" stroke-linejoin="round"/>
  </svg>
  <svg class="arrow" style="left:282px;top:711px;" width="58" height="84" viewBox="0 0 58 84" aria-hidden="true">
    <path d="M16 3 L40 3 L42 44 L56 44 L29 81 L2 44 L16 44 Z" fill="var(--yellow)" stroke="var(--ink)" stroke-width="3" stroke-linejoin="round"/>
  </svg>
  <svg class="arrow" style="left:534px;top:1038px;" width="84" height="58" viewBox="0 0 84 58" aria-hidden="true">
    <path d="M3 18 L46 16 L46 3 L81 29 L46 55 L46 42 L3 42 Z" fill="var(--yellow)" stroke="var(--ink)" stroke-width="3" stroke-linejoin="round"/>
  </svg>
</main>
<style>
  /* sheet sits behind content */
  .frame::after {
    content: ""; position: absolute; left: 41px; top: 58px; width: 743px; height: 1049px;
    background: var(--panel);
  }
</style>
</body>
</html>
```